Boracay Wedding Invitation Design

Hello, We would like a wedding invitation design for our wedding in Boracay. We would like it somewhat in the form of a boarding pass with beachy fresh colours, possibly a nice Boracay beach in the background Double sided with an envelope design to match. Maybe something simple on the envelope like a nice picture in the bottom left corner of a shell on a beach or something similar.

I would also like on the opposite side of the invite to be an "information sheet" with a matching beach design

The text files for both sides are included and i have also included 2 designs that i thought looked nice and are similar to what we are after.
Updates

Hello, I have updated the brief to be more specific with text files and images to make it easier for you. Thank you :)

Industry/Entity Type

Wedding

Font styles to use
Decorative
Script

Colors
fbee3d
33a6d7
33b8a4
fbf289
85cae6
ffffff

Requirements
Must have
• I would like to have this quote somewhere on the invitation
• This day I will marry my best friend,
• the one I laugh with,
• live for,
• dream with,
• love
• Owen & Marisa
• Request the pleasure of your company to celebrate their wedding
• On Friday the 17th March 2017
• at
• Velunda Grand Suites
• Boracay, Philippines
• Ceremony begins at 3.00pm
• RSVP
• Owen 0431907254
• Marisa 0417283649
• by
• 17th Jan 2016
• Dress: Beach Formal
• For the "information sheet"
• There will be a 5% discount on rooms booked at the Velunda under the event Owen & Marisa Wedding. The resort has a total of 24 rooms it would be nice if the majority of guests could stay at the resort from the night before until the night after the wedding but if you choose to stay elsewhere on the island there are plenty of other places to stay for cheaper and everything is fairly close as its a small island.
• We have currently blocked room stay for a short period of time so our guests can book rooms. If you choose to do so please email reservations@velundastays.example. Once rooms become available to the public again, towards the end of Jan, it will be first come first served basis. The resort is very popular so im assuming once this happens the rooms will be booked out.
• If you would like to check out the resort itself the website is www.velundagrand-isle.example
• We know its a fair distance to travel but we would really love to see you all there to celebrate and maybe even enjoy a small holiday while your here its a beautiful part of the world.
• If anyone has any questions please feel free to contact Owen on 0431907254
Nice to have
• A nice picture of a Boracay beach in the background would be nice

```html
<!DOCTYPE html>
<html lang="en">
<head>
<meta charset="utf-8">
<title>Owen &amp; Marisa — Wedding Invitation</title>
<link rel="stylesheet" href="https://fonts.googleapis.com/css2?family=Pinyon+Script&family=Kurale&family=Noticia+Text:ital@1&family=Open+Sans:wght@400&display=swap">
<style>
  :root {
    --paper: #f4efe4;
    --paper-edge: #ece5d6;
    --stub: #8d7667;
    --stub-text: #f3ece0;
    --teal-text: #4b9996;
    --ink: #4a3f3a;
    --venue: #6b5d55;
    --sea: #72c6cb;
    --cream: #f5f1e2;
    --palm-yellow: #cfc52d;
    --palm-green: #6ea83c;
  }
  html, body {
    margin: 0;
    padding: 0;
    width: 1200px;
    height: 509px;
    overflow: hidden;
    background: #ffffff;
  }
  .invitation {
    position: relative;
    width: 1200px;
    height: 509px;
    overflow: hidden;
    background: radial-gradient(ellipse at 40% 45%, var(--paper) 0%, var(--paper-edge) 100%);
    font-family: "Kurale", Georgia, serif;
  }
  .stub {
    position: absolute;
    left: 0; top: 0;
    width: 112px; height: 509px;
    background: var(--stub);
  }
  .stub-notch {
    position: absolute;
    left: 98px; top: 240px;
    width: 28px; height: 28px;
    border-radius: 50%;
    background: var(--stub);
  }
  .stub-label {
    position: absolute;
    left: 61px; top: 255px;
    transform: translate(-50%, -50%) rotate(-90deg);
    white-space: nowrap;
    font-family: "Open Sans", Arial, sans-serif;
    font-size: 18.5px;
    letter-spacing: 0.2px;
    color: var(--stub-text);
  }
  .quote-panel {
    position: absolute;
    left: 894px; top: 0;
    width: 306px; height: 509px;
    background: var(--sea);
  }
  .quote-notch {
    position: absolute;
    left: 878px; top: 239px;
    width: 32px; height: 32px;
    border-radius: 50%;
    background: var(--sea);
  }
  .swirl-ornament {
    position: absolute;
    left: 941px; top: 0;
    width: 242px; height: 158px;
    border-radius: 0 0 120px 120px;
    background: radial-gradient(ellipse at 50% 35%, rgba(245,241,226,0.75), rgba(245,241,226,0.15) 75%);
  }
  .palm-scene {
    position: absolute;
    left: 771px; top: 312px;
    width: 168px; height: 197px;
    border-radius: 60px 60px 0 0;
    background: linear-gradient(100deg, var(--palm-yellow) 0%, var(--palm-yellow) 60%, var(--palm-green) 100%);
    opacity: 0.85;
  }
  .wedding-vow {
    position: absolute;
    left: 894px; top: 220px;
    width: 312px;
    margin: 0;
    text-align: center;
    font-family: "Noticia Text", Georgia, serif;
    font-style: italic;
    font-size: 19.5px;
    line-height: 24.3px;
    color: var(--cream);
  }
  .details {
    position: absolute;
    left: 165px; top: 0;
    width: 600px;
    text-align: center;
    color: var(--ink);
  }
  .couple {
    position: absolute;
    left: -60px; top: 20px;
    width: 720px;
    margin: 0;
    font-family: "Pinyon Script", cursive;
    font-weight: 400;
    font-size: 78px;
    line-height: 1;
    color: var(--teal-text);
  }
  .request, .date, .at, .venue, .ceremony, .rsvp, .dress {
    position: absolute;
    left: 0; width: 600px;
    margin: 0;
  }
  .request { top: 158px; font-size: 19px; }
  .date { top: 203px; font-size: 25.5px; color: var(--teal-text); }
  .at { top: 234px; font-size: 17px; }
  .venue { top: 253px; font-size: 22.5px; color: var(--venue); }
  .ceremony { top: 305px; font-size: 18.5px; }
  .rsvp { top: 351px; font-size: 17px; line-height: 20.5px; }
  .dress { top: 452px; font-size: 17px; }
</style>
</head>
<body>
<main class="invitation">
  <div class="stub"></div>
  <div class="stub-notch"></div>
  <div class="stub-label">FULL INFORMATION AVAILABLE AT THE BACK</div>

  <div class="quote-panel"></div>
  <div class="quote-notch"></div>
  <div class="swirl-ornament" role="img" aria-label="Cream flourish of curling swirls"></div>
  <div class="palm-scene" role="img" aria-label="Illustration of yellow and green palm trees"></div>

  <section class="details">
    <h1 class="couple">Owen &amp; Marisa</h1>
    <p class="request">Request the pleasure of your company to celebrate their wedding</p>
    <p class="date">On Friday the 17th March 2017</p>
    <p class="at">at</p>
    <p class="venue">Velunda Grand Suites, Boracay, Philippines</p>
    <p class="ceremony">Ceremony begins at 3.00pm</p>
    <p class="rsvp">RSVP<br>Owen 0431907254<br>Marisa 0417283649<br>by 17th Jan 2016</p>
    <p class="dress">Dress: Beach Formal</p>
  </section>

  <p class="wedding-vow">This day<br>I will marry my best friend,<br>the one I laugh with,<br>live for,<br>dream with,<br>love</p>
</main>
</body>
</html>
```